Business card for Verano Living

Hi again, I need a business card for my Verano Living business you have been working on with the following information:

Clara Hollis
Director
m. 0412 736 258
e. clara@veranoliving-example.com.au
w. www.veranoliving-example.com.au

Maybe you could use the original design (using both the green & white) and where the white box is you could include the above details (name / mobile / etc) - Perhaps the 'i' in Clara could be the bow tie again?

Then the back could be green with black writing stating:

Services Offered:

* Personal Assistant Concierge
* Decluttering Concierge
* Home Management Concierge
* FIFO Concierge
* Events Concierge
* Leisure & Travel Concierge
* Seasonal Concierge
* Professional Concierge

Many thanks
Updates

Hi Everyone I'm really sorry but I am working with just one designer on this brief, thank you for your work and apologies for my error.

Industry/Entity Type

Business

```html
<!DOCTYPE html>
<html lang="en">
<head>
<meta charset="utf-8">
<title>Verano Living — Business Card</title>
<link rel="stylesheet" href="https://fonts.googleapis.com/css2?family=Open+Sans:wght@400;600&family=Comfortaa:wght@600;700&display=swap">
<style>
  :root {
    --lime: #a8f500;
    --lime-soft: #c6f77a;
    --white: #ffffff;
    --grey-band: #e2e2e2;
    --text-green: #5f9a12;
    --panel-dark: #47a01b;
    --panel-light: #62c22f;
    --mint: #8ef2c8;
    --teal: #58b995;
    --footer-blue: #2340ff;
    --shadow: rgba(20, 40, 10, 0.75);
  }
  * { box-sizing: border-box; margin: 0; padding: 0; }
  html, body { width: 900px; height: 1200px; overflow: hidden; background: var(--white); }
  .canvas { position: relative; width: 900px; height: 1200px; overflow: hidden; background: var(--white); }

  /* Front of card */
  .card-front { position: absolute; left: 0; top: 0; width: 900px; height: 545px; background: var(--lime); overflow: hidden; }
  .card-front .waves { position: absolute; inset: 0; }
  .square-grid { position: absolute; left: 27px; top: 147px; width: 326px; height: 125px;
    background: linear-gradient(180deg, rgba(255,255,255,0.35), rgba(255,255,255,0.2)); }
  .flower-left { position: absolute; left: 0; top: 248px; width: 370px; height: 297px;
    background: radial-gradient(ellipse at 30% 55%, var(--mint) 0%, var(--lime-soft) 55%, rgba(168,245,0,0) 75%); }
  .flower-right { position: absolute; left: 750px; top: 5px; width: 150px; height: 150px;
    background: radial-gradient(circle at 65% 40%, var(--mint) 0%, var(--lime-soft) 50%, rgba(255,255,255,0) 72%); }

  .contact-box { position: absolute; left: 476px; top: 187px; width: 359px; height: 164px;
    background: var(--white); border: 3px solid var(--lime); box-shadow: 1px 2px 0 #8a8a8a;
    padding: 34px 0 0 56px; font-family: "Open Sans", sans-serif; color: var(--text-green); }
  .contact-name { font-size: 21px; font-weight: 600; line-height: 1.2; margin-bottom: 4px; }
  .contact-line { font-size: 14.5px; line-height: 1.12; }

  /* Back of card */
  .card-back { position: absolute; left: 12px; top: 557px; width: 881px; height: 525px; background: var(--panel-dark); overflow: hidden; }
  .card-back .wave { position: absolute; inset: 0; }
  .services-title { position: absolute; left: 0; right: 0; top: 52px; text-align: center;
    font-family: "Open Sans", sans-serif; font-weight: 600; font-size: 39px; color: var(--white);
    text-shadow: 2px 2px 2px var(--shadow); letter-spacing: 0.5px; }
  .services-title .initial { font-size: 72px; line-height: 1; }
  .services-list { position: absolute; left: 164px; top: 163px; list-style: none;
    font-family: "Comfortaa", sans-serif; font-weight: 700; font-size: 28px; line-height: 37.6px;
    letter-spacing: 2.4px; word-spacing: 6px; color: var(--white); text-shadow: 2px 2px 2px var(--shadow); }
  .services-list li::before { content: "* "; }

  .footer-band { position: absolute; left: 0; top: 1092px; width: 900px; height: 108px; background: var(--footer-blue); }
</style>
</head>
<body>
<main class="canvas">
  <section class="card-front" aria-label="Card front">
    <svg class="waves" width="900" height="545" viewBox="0 0 900 545" aria-hidden="true">
      <path d="M0,330 C250,250 500,70 760,0 L900,0 L900,530 C700,440 460,395 260,412 C150,422 60,440 0,452 Z" fill="#ffffff"/>
      <path d="M0,318 C300,220 540,50 790,-5" fill="none" stroke="#e2e2e2" stroke-width="22"/>
      <path d="M220,352 C460,322 700,380 900,452" fill="none" stroke="#e2e2e2" stroke-width="30"/>
    </svg>
    <div class="square-grid" role="img" aria-label="Decorative grid of soft light squares"></div>
    <div class="flower-left" role="img" aria-label="Decorative mint and lime petal flower with concentric circles"></div>
    <div class="flower-right" role="img" aria-label="Small decorative petal flower with concentric circles"></div>
    <div class="contact-box">
      <p class="contact-name">Clara Hollis</p>
      <p class="contact-line">Director</p>
      <p class="contact-line">0412 736 258</p>
      <p class="contact-line">clara@veranoliving-example.com.au</p>
      <p class="contact-line">www.veranoliving-example.com.au</p>
    </div>
  </section>

  <section class="card-back" aria-label="Card back">
    <svg class="wave" width="881" height="525" viewBox="0 0 881 525" aria-hidden="true">
      <path d="M0,155 C180,140 300,190 450,260 C600,330 760,360 881,305 L881,525 L0,525 Z" fill="#62c22f"/>
    </svg>
    <h2 class="services-title"><span class="initial">S</span>ervices Offered:</h2>
    <ul class="services-list">
      <li>Personal Assistant Concierge</li>
      <li>Decluttering Concierge</li>
      <li>Home Management Concierge</li>
      <li>FIFO Concierge</li>
      <li>Events Concierge</li>
      <li>Leisure &amp; Travel Concierge</li>
      <li>Seasonal Concierge</li>
      <li>Professional Concierge</li>
    </ul>
  </section>

  <div class="footer-band"></div>
</main>
</body>
</html>
```